Business Card Design for a Personal Trainer

I need a business card design for my job as a personal trainer. It should have a unique, modern and exclusive design. On the front there should be only my logo with my name and my job. 0163/2918374 Tobias Kellinger Lindenfeldweg 14 80412 Munich Germany The most important contact information is the web adress. it can be bigger than the rest, but its not necessary. The card should be 8,5cmx5,5cm big. Font: Roboto. Colors: black, white, gray, 56c1ff.

```html
<!DOCTYPE html>
<html lang="de">
<head>
<meta charset="utf-8">
<title>Tobias Kellinger – Visitenkarte</title>
<link rel="stylesheet" href="https://fonts.googleapis.com/css2?family=Roboto:wght@300;400;500;700&display=swap">
<style>
  :root {
    --page-bg: #ebebeb;
    --card-bg: #050505;
    --band-bg: #161616;
    --white: #ffffff;
    --soft-white: #e6e6e6;
    --photo-dark: #1c1c1c;
    --photo-light: #5a5a5a;
  }
  * { margin: 0; padding: 0; box-sizing: border-box; }
  html, body {
    width: 924px; height: 1200px; overflow: hidden;
    background: var(--page-bg);
    font-family: "Roboto", Arial, sans-serif;
    color: var(--white);
  }
  .sheet { position: relative; width: 924px; height: 1200px; }
  .card {
    position: absolute; left: 58px; width: 808px; height: 522px;
    background: var(--card-bg);
    overflow: hidden;
    box-shadow: 6px 8px 10px rgba(0,0,0,0.35);
  }
  .card--front { top: 68px; }
  .card--back { top: 617px; }

  /* Front */
  .front__wordmark {
    position: absolute; left: 0; right: 0; top: 185px;
    text-align: center; font-weight: 700; font-size: 40px; letter-spacing: 6px;
  }
  .front__name {
    position: absolute; left: 0; right: 0; top: 291px;
    text-align: center; font-weight: 400; font-size: 42px; letter-spacing: 0.5px;
  }
  .front__role {
    position: absolute; left: 214px; width: 380px; top: 346px;
    display: flex; align-items: center; gap: 8px;
    font-size: 16px; letter-spacing: 4px; font-weight: 400;
  }
  .front__role::before, .front__role::after {
    content: ""; flex: 1; height: 1.5px; background: var(--white);
  }
  .front__web {
    position: absolute; left: 0; right: 0; top: 450px;
    text-align: center; font-size: 19px; font-weight: 300; letter-spacing: 2.5px;
  }

  /* Back */
  .back__frame {
    position: absolute; left: 60px; top: 35px; width: 326px; height: 452px;
    border: 1.5px solid var(--white);
  }
  .back__photo {
    position: absolute; left: 120px; top: 52px; width: 240px; height: 470px;
    background: linear-gradient(180deg, var(--photo-light), var(--photo-dark));
    border-radius: 100px 100px 0 0;
  }
  .back__band {
    position: absolute; left: 262px; top: 69px; width: 546px; height: 58px;
    background: var(--band-bg);
  }
  .back__name {
    position: absolute; left: 472px; top: 95px;
    font-size: 19px; font-weight: 700; letter-spacing: 3.5px;
  }
  .contact { position: absolute; left: 480px; list-style: none; }
  .contact__item {
    position: absolute; left: 0; width: 320px;
    display: flex; align-items: flex-start; gap: 22px;
    font-size: 18px; font-weight: 300; letter-spacing: 1.8px; line-height: 24px;
    color: var(--soft-white);
  }
  .contact__icon { width: 14px; height: 14px; margin-top: 5px; flex: none; fill: var(--white); }
  .contact__item--phone { top: 182px; }
  .contact__item--mail { top: 226px; }
  .contact__item--address { top: 268px; }
  .back__wordmark {
    position: absolute; left: 500px; width: 202px; top: 408px;
    text-align: center; font-weight: 700; font-size: 22px; letter-spacing: 4px;
  }
</style>
</head>
<body>
<main class="sheet">
  <section class="card card--front">
    <div class="front__wordmark">KELLINGER</div>
    <h1 class="front__name">TOBIAS KELLINGER</h1>
    <p class="front__role">PERSONAL TRAINER</p>
    <p class="front__web">www.tobiaskellinger.de</p>
  </section>

  <section class="card card--back">
    <div class="back__frame"></div>
    <div class="back__band"></div>
    <div class="back__photo" role="img" aria-label="Schwarz-weiß Porträtfoto des Trainers mit verschränkten Armen im Langarmshirt"></div>
    <h2 class="back__name">TOBIAS KELLINGER</h2>
    <ul class="contact">
      <li class="contact__item contact__item--phone">
        <svg class="contact__icon" viewBox="0 0 24 24" aria-hidden="true"><path d="M6.6 10.8a15.1 15.1 0 0 0 6.6 6.6l2.2-2.2a1 1 0 0 1 1-.25 11.4 11.4 0 0 0 3.6.57 1 1 0 0 1 1 1V20a1 1 0 0 1-1 1A17 17 0 0 1 3 4a1 1 0 0 1 1-1h3.5a1 1 0 0 1 1 1c0 1.25.2 2.45.57 3.57a1 1 0 0 1-.25 1z"/></svg>
        <span>0163/2918374</span>
      </li>
      <li class="contact__item contact__item--mail">
        <svg class="contact__icon" viewBox="0 0 24 24" aria-hidden="true"><path d="M2 5h20v14H2z M3.5 6.5 12 13l8.5-6.5" fill="none" stroke="#fff" stroke-width="2"/></svg>
        <span>kellinger@postfach-mail.de</span>
      </li>
      <li class="contact__item contact__item--address">
        <svg class="contact__icon" viewBox="0 0 24 24" aria-hidden="true"><path d="M12 2a7 7 0 0 0-7 7c0 5 7 13 7 13s7-8 7-13a7 7 0 0 0-7-7z" fill="none" stroke="#fff" stroke-width="2"/><circle cx="12" cy="9" r="2.5" fill="none" stroke="#fff" stroke-width="2"/></svg>
        <span>Lindenfeldweg 14<br>80412 München</span>
      </li>
    </ul>
    <div class="back__wordmark">KELLINGER</div>
  </section>
</main>
</body>
</html>
```